Large multi-office optometry business opening a Dry Eye Spa and needs sign.

Business name/sign info: Brenwick Dry Eye Institute, (555) 362-4817
Backlit pole sign at office entrance on a very busy street
Sign dimensions: 53" tall x 136.5" wide
State of the art Dry Eye Spa for treatment of all forms of dry eye and ocular surface disease. Also, have aesthetics treatments (IPL, Low Level Light Treatment, etc.)

Target Market(s)

People who are suffering from: dryness, burning, foreign body sensation, itching, fluctuating vision, tired eyes, etc.

Industry/Entity Type

Optometry and aesthetics

Colors
0054AA
0677BA
7BADD7
CADEEF
E8F1F8

Requirements
Must have
• Business name, phone number, subliminal message of relief in a glance or short look.
Nice to have
• Cool, relief, soothing sense.
Should not have
• Too much information or too busy.

```html
<!DOCTYPE html>
<html lang="en">
<head>
<meta charset="utf-8">
<title>Brenwick Dry Eye Institute – Pole Sign</title>
<link rel="stylesheet" href="https://fonts.googleapis.com/css2?family=Oswald:wght@400;500;600;700&display=swap">
<style>
  :root {
    --page-bg: #eef1f4;
    --sign-bg: #ffffff;
    --brand-blue: #0a62ad;
    --deep-blue: #0054aa;
    --wave-blue: #0d4f91;
    --wave-blue-dark: #0a3f78;
    --mid-blue: #0677ba;
    --soft-blue: #7badd7;
    --pale-blue: #cadeef;
    --mist-blue: #e8f1f8;
    --accent-red: #e32124;
    --white: #ffffff;
  }
  html, body {
    margin: 0;
    padding: 0;
    width: 972px;
    height: 1200px;
    overflow: hidden;
    background: var(--page-bg);
  }
  .canvas {
    position: relative;
    width: 972px;
    height: 1200px;
  }
  .sign {
    position: absolute;
    left: 36px;
    top: 425px;
    width: 900px;
    height: 350px;
    box-shadow: 0 14px 30px rgba(0, 0, 0, 0.18);
    background: var(--sign-bg);
  }
  .sign svg { display: block; }
  .brand-name {
    font-family: "Oswald", sans-serif;
    font-weight: 500;
    fill: var(--deep-blue);
    letter-spacing: 1px;
  }
  .headline {
    font-family: "Oswald", sans-serif;
    font-weight: 600;
    fill: var(--brand-blue);
  }
  .pill-label {
    font-family: "Oswald", sans-serif;
    font-weight: 600;
    fill: var(--white);
  }
  .phone {
    font-family: "Oswald", sans-serif;
    font-weight: 500;
    fill: var(--deep-blue);
  }
</style>
</head>
<body>
<main class="canvas">
  <section class="sign" aria-label="Brenwick Dry Eye Institute sign">
    <svg width="900" height="350" viewBox="0 0 900 350" xmlns="http://www.w3.org/2000/svg">
      <defs>
        <linearGradient id="waveFill" x1="0" y1="0" x2="0" y2="1">
          <stop offset="0" stop-color="#0d4f91"/>
          <stop offset="1" stop-color="#0a3f78"/>
        </linearGradient>
        <radialGradient id="eyeLarge" cx="0.55" cy="0.45" r="0.6">
          <stop offset="0" stop-color="#e9cfc4"/>
          <stop offset="1" stop-color="#c99f8c"/>
        </radialGradient>
        <radialGradient id="eyeSide" cx="0.5" cy="0.5" r="0.6">
          <stop offset="0" stop-color="#c88a5c"/>
          <stop offset="1" stop-color="#8a5a3c"/>
        </radialGradient>
        <radialGradient id="examPhoto" cx="0.5" cy="0.5" r="0.6">
          <stop offset="0" stop-color="#9aa2a8"/>
          <stop offset="1" stop-color="#5d656b"/>
        </radialGradient>
      </defs>

      <path class="wave-band" d="M0 239 C 160 215, 300 250, 420 290 C 500 318, 560 332, 620 330 C 720 326, 820 270, 900 217 L 900 350 L 0 350 Z" fill="url(#waveFill)"/>
      <path class="wave-edge" d="M0 239 C 160 215, 300 250, 420 290 C 500 318, 560 332, 620 330 C 720 326, 820 270, 900 217" fill="none" stroke="var(--accent-red)" stroke-width="4"/>

      <g class="medallion" role="img" aria-label="Close-up photo of an irritated eye held open by a finger">
        <circle cx="160" cy="114" r="104" fill="url(#eyeLarge)" stroke="var(--accent-red)" stroke-width="6"/>
      </g>
      <g class="medallion" role="img" aria-label="Side-view photo of a brown eye with long lashes">
        <circle cx="94" cy="212" r="64" fill="url(#eyeSide)" stroke="var(--accent-red)" stroke-width="6"/>
      </g>
      <g class="medallion" role="img" aria-label="Photo of a patient behind an eye-exam phoropter">
        <circle cx="209" cy="244" r="45" fill="url(#examPhoto)" stroke="var(--accent-red)" stroke-width="5"/>
      </g>

      <text class="brand-name" x="612" y="50" font-size="19" text-anchor="middle">HALVERN FAMILY</text>
      <text class="brand-name" x="612" y="78" font-size="25" text-anchor="middle">EYE CARE</text>

      <path class="bracket" d="M406 228 H353 V139 H367 M830 139 H845 V228 H792" fill="none" stroke="var(--accent-red)" stroke-width="1.5"/>

      <text class="headline" x="598" y="189" font-size="120" text-anchor="middle" textLength="462" lengthAdjust="spacingAndGlyphs">BRENWICK</text>

      <rect class="pill" x="406" y="203" width="386" height="51" rx="10" fill="var(--accent-red)" stroke="var(--soft-blue)" stroke-width="3"/>
      <text class="pill-label" x="599" y="243" font-size="38" text-anchor="middle" textLength="358" lengthAdjust="spacingAndGlyphs">DRY EYE INSTITUTE</text>

      <text class="phone" x="601" y="300" font-size="44" text-anchor="middle" textLength="249" lengthAdjust="spacingAndGlyphs">(555) 362-4817</text>
    </svg>
  </section>
</main>
</body>
</html>
```